Packaging sleeve for food containers

I have designed eco-friendly food prep containers that come in packs of 10. The food containers are beige with a clear lid. I need a design for a cardboard sleeve that wraps around the containers as part of the packaging with all of the information on it. I will upload a basic idea of what I am looking for as well as 2 other similar brands for comparison. I have a template with the information I require to be included but I need the final design to be jazzed up to a professional standard. I need help with colours and the design of the sleeve.

Target Market(s)

People who like to meal prep their food in advance and who might also be environmentally conscious. Female and male, somewhat health conscious. Might be looking to lose or maintain weight or just improve nutrition. Organised people. Age range 20-50(ish).

Font styles to use
Serif
Sans Serif

Requirements
Must have
• The information contained in my example sleeve
Nice to have
• Harmonious colours

```html
<!DOCTYPE html>
<html lang="en">
<head>
<meta charset="utf-8">
<title>Pack n Plate – Meal Prep Containers Sleeve</title>
<link href="https://fonts.googleapis.com/css2?family=Archivo+Black&family=Roboto:wght@400;700&family=Space+Mono:wght@700&display=swap" rel="stylesheet">
<style>
  :root{
    --bg:#e7ebf2;
    --green:#157650;
    --green-line:#2a9aa0;
    --amber:#f7b21c;
    --orange:#f8a91a;
    --white:#ffffff;
    --wood-dark:#5a2f1d;
    --wood:#8a4b2c;
    --wood-light:#a8643d;
  }
  *{box-sizing:border-box;margin:0;padding:0}
  html,body{width:1200px;height:954px;overflow:hidden;background:var(--bg)}
  .sleeve{position:absolute;left:470px;top:13px;width:259px;height:928px;background:var(--green);font-family:"Roboto",sans-serif;color:var(--white)}
  .panel{position:absolute;left:0;width:259px;border-bottom:1px solid var(--green-line)}
  .panel--flap{top:0;height:192px}
  .panel--front{top:192px;height:300px;overflow:hidden}
  .panel--features{top:492px;height:191px}
  .panel--back{top:683px;height:245px;border-bottom:none}

  .flap-text{position:absolute;inset:0;transform:rotate(180deg);text-align:center;font-size:8px;line-height:1}
  .flap-text p{position:absolute;left:0;right:0;padding-left:20px}
  .social-square{display:inline-block;width:9px;height:9px;background:var(--white);vertical-align:-1px;margin:0 3px;border-radius:1px}

  .front-photo{position:absolute;inset:0;background:
      radial-gradient(circle at 85% 25%,#d9a12b 0,#c7402a 18%,transparent 42%),
      radial-gradient(circle at 80% 70%,#3a1f3a 0,transparent 25%),
      linear-gradient(100deg,var(--wood-light),var(--wood) 45%,var(--wood-dark))}
  .brand-ring{position:absolute;left:17px;top:17px;width:86px;height:86px;border:1.5px solid #e9ddd0;border-radius:50%;display:flex;align-items:center;justify-content:center}
  .brand-name{font-family:"Space Mono",monospace;font-weight:700;font-size:8.5px;color:#f1e7dc;letter-spacing:.5px}
  .pack-badge{position:absolute;left:208px;top:19px;width:44px;height:44px;border-radius:50%;background:var(--white);border:2px solid var(--green);color:var(--green);font-weight:700;font-size:10.5px;line-height:1.05;display:flex;align-items:center;justify-content:center;text-align:center}
  .title-top{position:absolute;left:12px;top:117px;font-family:"Archivo Black",sans-serif;font-size:21px;letter-spacing:2px;color:var(--orange)}
  .title-main{position:absolute;left:11px;top:145px;font-family:"Archivo Black",sans-serif;font-size:21px;letter-spacing:1px;color:var(--white)}
  .subtitle{position:absolute;left:16px;top:190px;font-family:"Space Mono",monospace;font-weight:700;font-size:13px;color:var(--white)}
  .eco-band{position:absolute;left:0;top:220px;width:259px;height:28px;background:var(--amber);font-family:"Archivo Black",sans-serif;font-size:14px;letter-spacing:1.6px;line-height:28px;padding-left:13px;white-space:nowrap}
  .eco-band .g{color:var(--green)} .eco-band .w{color:var(--white)}
  .compartments{position:absolute;left:20px;top:262px}

  .feature-frame{position:absolute;left:49px;top:25px;width:157px;height:148px;border:1.5px solid var(--amber)}
  .feature-grid{position:absolute;inset:8px 6px;display:grid;grid-template-columns:repeat(3,1fr);grid-template-rows:repeat(3,1fr)}
  .feature{display:flex;flex-direction:column;align-items:center;color:var(--amber);font-size:4.5px;font-weight:700;text-align:center;line-height:1}
  .feature svg{width:30px;height:30px;margin-bottom:1px}

  .back-ring{position:absolute;left:77px;top:61px;width:106px;height:106px;border:2px solid var(--white);border-radius:50%;display:flex;align-items:center;justify-content:center}
  .back-ring .brand-name{color:var(--white);font-size:10px;letter-spacing:1px}
  .web-band{position:absolute;left:0;top:195px;width:259px;height:20px;background:var(--amber);text-align:center;font-size:11px;letter-spacing:1px;line-height:20px;color:var(--white)}
  .trim-line{position:absolute;left:0;top:236px;width:259px;border-top:1px solid var(--green-line)}
</style>
</head>
<body>
<main class="sleeve">
  <section class="panel panel--flap">
    <div class="flap-text">
      <p style="top:56px">Winner Winner Meal Prep dinner!</p>
      <p style="top:72px">Tag us @PacknPlate on <span class="social-square"></span> with</p>
      <p style="top:87px">your containers to win monthly prizes</p>
      <p style="top:115px">Connect with us</p>
      <p style="top:131px">www.packnplate.com.au</p>
      <p style="top:146px">@PacknPlate <span class="social-square"></span></p>
    </div>
  </section>

  <section class="panel panel--front">
    <div class="front-photo" role="img" aria-label="Photo of fresh vegetables, tomatoes, peppers, eggplant and spaghetti on a wooden table"></div>
    <div class="brand-ring"><span class="brand-name">Pack n Plate</span></div>
    <div class="pack-badge">10<br>Pack</div>
    <h1 class="title-top">Meal Prep</h1>
    <h2 class="title-main">CONTAINERS</h2>
    <p class="subtitle">3 compartment</p>
    <p class="eco-band"><span class="g">Eco Friendly</span> <span class="w">Wheatstraw</span></p>
    <svg class="compartments" width="48" height="30" viewBox="0 0 48 30" fill="none" stroke="#f7b21c" stroke-width="1.5" font-family="Roboto,sans-serif" font-weight="700" font-size="8">
      <rect x="1" y="1" width="46" height="28" rx="2"/>
      <rect x="4" y="4" width="18" height="22" rx="4"/>
      <rect x="26" y="4" width="18" height="10" rx="4"/>
      <rect x="26" y="16" width="18" height="10" rx="4"/>
      <text x="7" y="18" fill="#ffffff" stroke="none">2c</text>
      <text x="30" y="12" fill="#ffffff" stroke="none" font-size="7">1c</text>
      <text x="30" y="24" fill="#ffffff" stroke="none" font-size="7">1c</text>
    </svg>
  </section>

  <section class="panel panel--features">
    <div class="feature-frame">
      <div class="feature-grid">
        <div class="feature"><svg viewBox="0 0 30 30" fill="none" stroke="currentColor" stroke-width="1.5"><circle cx="15" cy="15" r="13.5"/><rect x="7" y="10" width="16" height="10" rx="1"/><rect x="9" y="12" width="9" height="6"/></svg>Microwave<br>Safe</div>
        <div class="feature"><svg viewBox="0 0 30 30" fill="none" stroke="currentColor" stroke-width="1.5"><circle cx="15" cy="15" r="13.5"/><path d="M15 7v16M8 11l14 8M8 19l14-8"/></svg>Freezer<br>Safe</div>
        <div class="feature"><svg viewBox="0 0 30 30" fill="none" stroke="currentColor" stroke-width="1.5"><circle cx="15" cy="15" r="13.5"/><circle cx="13" cy="18" r="4"/><circle cx="18" cy="18" r="4"/><path d="M9 11l3-4M13 11l3-4M17 11l3-4"/></svg>Dishwasher<br>Safe</div>
        <div class="feature"><svg viewBox="0 0 30 30" fill="none" stroke="currentColor" stroke-width="1.5"><circle cx="15" cy="15" r="13.5"/><text x="6" y="15" font-size="7" fill="currentColor" stroke="none" font-family="Roboto,sans-serif">BPA</text><text x="5" y="22" font-size="6" fill="currentColor" stroke="none" font-family="Roboto,sans-serif">FREE</text></svg>BPA Free</div>
        <div class="feature"><svg viewBox="0 0 30 30" fill="none" stroke="currentColor" stroke-width="1.5"><circle cx="15" cy="15" r="13.5"/><path d="M15 8v15M15 12l-4-3M15 12l4-3M15 16l-4-3M15 16l4-3"/></svg>Wheatstraw</div>
        <div class="feature"><svg viewBox="0 0 30 30" fill="none" stroke="currentColor" stroke-width="1.5"><circle cx="15" cy="15" r="13.5"/><path d="M15 7l7 14H8z"/><path d="M6 22L24 8"/></svg>Leakproof</div>
        <div class="feature"><svg viewBox="0 0 30 30" fill="none" stroke="currentColor" stroke-width="1.5"><circle cx="15" cy="15" r="13.5"/><path d="M6 11h18M5 14h20M5 17h20M6 20h18"/></svg>Stackable</div>
        <div class="feature"><svg viewBox="0 0 30 30" fill="none" stroke="currentColor" stroke-width="1.2"><circle cx="15" cy="15" r="13.5"/><circle cx="9" cy="11" r="3"/><circle cx="15" cy="11" r="3"/><circle cx="21" cy="11" r="3"/><circle cx="9" cy="19" r="3"/><circle cx="15" cy="19" r="3"/><circle cx="21" cy="19" r="3"/></svg>Reusable</div>
        <div class="feature"><svg viewBox="0 0 30 30" fill="none" stroke="currentColor" stroke-width="1.5"><circle cx="15" cy="15" r="13.5"/><path d="M12 9l3-3 3 3M21 13l1 5-5 1M9 20l-2-4 4-2"/><path d="M15 6l4 7M22 18h-9M7 16l4-7"/></svg>Recycle</div>
      </div>
    </div>
  </section>

  <section class="panel panel--back">
    <div class="back-ring"><span class="brand-name">Pack n Plate</span></div>
    <p class="web-band">www.packnplate.com.au</p>
    <div class="trim-line"></div>
  </section>
</main>
</body>
</html>
```